Creative - Appealing - Business Card Design Project

Looking for a Business card design (vector artwork) for an existing company called 'Copperfield Sound'. We operate in the entertainment industry specializing in audio system design and rental, however; we also deal with other sectors of the entertainment industry including lighting, video, staging and power system design and rental. We would like to see designs that don't focus too much on audio but include elements encompassing everything else.

Double sided business card, following our new colour scheme and logo, which is attached. The card would ideally be creative and eye catching to draw in new customers in the elegant event production market, such as weddings & corporate affairs.

Target Market(s)

High end corporate clients, wedding clients

Industry/Entity Type

Entertainment

Requirements
Must have
• Our contact details, these can be worded & listed however you think appropriate as part as the design

Business Name - Copperfield Sound
My Name - Benedict Thornbury
Web Address - www.copperfieldsound-example.com
Mobile Number - 07914 362 517
Office Number - 0330 411 7785
Email - ben@copperfieldsound-example.com

The name, email and mobile number would need to be able to be changed to my business partners also.

The font used on our logo is Sansation
Nice to have
• On one side maybe a word cloud involving the services in which we can provide; Lighting, Sound, Event Production, Staging, LED Uplighting, Projection Mapping, Wedding Hire

On the other side, all the important credentials of contact.
Should not have
• The design should not use any old style fonts (i.e Times New Roman, Gothic etc) or on the other side of the scale, any 'jokey' fonts (i.e. Comic Sans).

The font to be used is Sansation

```html
<!DOCTYPE html>
<html lang="en">
<head>
<meta charset="utf-8">
<title>Copperfield Sound – Business Card</title>
<link href="https://fonts.googleapis.com/css2?family=Play:wght@400;700&display=swap" rel="stylesheet">
<style>
  :root {
    --backdrop: #262628;
    --purple: #5a3796;
    --purple-deep: #4a2b82;
    --purple-light: #6d4bab;
    --card-white: #efeff2;
    --card-grey: #e2e2e8;
    --silver: #c9c9d0;
    --grey-text: #8a8a90;
    --brand-grey: #9a9aa0;
  }
  * { margin: 0; padding: 0; box-sizing: border-box; }
  html, body {
    width: 1200px; height: 900px; overflow: hidden;
    background: var(--backdrop);
    font-family: "Play", sans-serif;
  }
  .canvas { position: relative; width: 1200px; height: 900px; }

  .card {
    position: absolute; top: 275px;
    width: 540px; height: 350px;
    overflow: hidden;
    box-shadow: 0 12px 30px rgba(0,0,0,.45);
  }
  .card-front { left: 40px; }
  .card-back  { left: 620px; background: var(--card-white); }

  .front-backdrop {
    position: absolute; inset: 0;
    background: linear-gradient(120deg, var(--purple-light) 0%, var(--purple) 45%, var(--purple-deep) 100%);
  }
  .back-backdrop {
    position: absolute; inset: 0;
    background: linear-gradient(160deg, var(--card-white) 0%, var(--card-grey) 100%);
  }
  .back-accent {
    position: absolute; left: 0; right: 0; bottom: 0; height: 90px;
    background: linear-gradient(180deg, var(--purple-light) 0%, var(--purple-deep) 100%);
  }

  /* front */
  .front-brand {
    position: absolute; left: 50px; top: 138px;
    display: flex; align-items: center; gap: 16px;
  }
  .brand-mark {
    width: 46px; height: 46px; border-radius: 50%;
    background: var(--silver); flex: none;
  }
  .front-name {
    font-size: 34px; font-weight: 700; letter-spacing: .5px;
    color: var(--silver); text-transform: uppercase; line-height: 1;
  }
  .front-web {
    position: absolute; left: 112px; top: 184px;
    font-size: 12px; letter-spacing: 3px; color: var(--silver);
  }
  .services {
    position: absolute; left: 40px; right: 40px; top: 222px;
    text-align: center; font-size: 13.5px; line-height: 1.45;
    color: var(--silver);
  }
  .services .sep { padding: 0 5px; }

  /* back */
  .back-brand {
    position: absolute; left: 34px; top: 96px;
    display: flex; flex-direction: column; align-items: flex-start; gap: 12px;
  }
  .back-brand .brand-mark { width: 40px; height: 40px; background: var(--purple); }
  .back-name {
    font-size: 26px; font-weight: 700; color: var(--brand-grey);
    text-transform: uppercase; line-height: 1.05; width: 170px;
  }
  .contact {
    position: absolute; left: 226px; top: 92px; right: 20px;
    color: var(--grey-text); font-size: 13px;
  }
  .contact-name {
    font-size: 19px; color: var(--purple); margin-bottom: 8px; margin-left: 20px;
  }
  .contact-list { list-style: none; line-height: 1.4; }
  .contact-list .label { display: inline-block; width: 20px; }
  .contact-web { margin-top: 14px; }
</style>
</head>
<body>
<main class="canvas">

  <section class="card card-front" aria-label="Card front">
    <div class="front-backdrop" role="img" aria-label="Purple background with angular light-beam pattern"></div>
    <div class="front-brand">
      <span class="brand-mark"></span>
      <span class="front-name">Copperfield Sound</span>
    </div>
    <p class="front-web">www.copperfieldsound-example.com</p>
    <p class="services">
      Lighting<span class="sep">|</span>Sound<span class="sep">|</span>Event Production<span class="sep">|</span>Staging<span class="sep">|</span>LED Uplighting<br>
      Projection Mapping<span class="sep">|</span>Wedding Hire
    </p>
  </section>

  <section class="card card-back" aria-label="Card back">
    <div class="back-backdrop" role="img" aria-label="Light grey background with faint angular light-beam pattern"></div>
    <div class="back-accent" role="img" aria-label="Purple angular accent shapes"></div>
    <div class="back-brand">
      <span class="brand-mark"></span>
      <span class="back-name">Copperfield Sound</span>
    </div>
    <div class="contact">
      <p class="contact-name">Benedict Thornbury</p>
      <ul class="contact-list">
        <li><span class="label">M</span>07914 362 517</li>
        <li><span class="label">O</span>0330 411 7785</li>
        <li><span class="label">E</span>ben@copperfieldsound-example.com</li>
      </ul>
      <p class="contact-web">www.copperfieldsound-example.com</p>
    </div>
  </section>

</main>
</body>
</html>
```